General Dental Office Business Card

I run a private general dental office in southern California, and would like a refresh/redesign of my business card. I focus on quality care rather than volume. The email address on the uploaded current card should be updated to: info@marbleshoredental.example. The current card's logo is a deboss, but I am open to other ideas. The logo can be refreshed, but it is something that's been with me since the beginning of the office, so I wouldn't want a drastic redesign.
Target Market(s)
Adults 18-99, whoever needs dental services
Industry/Entity Type
Healthcare/Dental
Contact Information for Business Card
Name, Address, Phone, email
Colors
Designer to choose colors to be used in the design.
Requirements
Must have
- Logo (Same as original one in the uploaded file), space on back for appointment time/date

```html
<!DOCTYPE html>
<html lang="en">
<head>
<meta charset="utf-8">
<title>Marble Shore Dental – Business Card</title>
<link href="https://fonts.googleapis.com/css2?family=Quicksand:wght@400;700&display=swap" rel="stylesheet">
<style>
  :root {
    --backdrop: #dcdcdc;
    --card: #f6f6f6;
    --teal: #7fd6ea;
    --ink: #5f6168;
    --ink-dark: #45474d;
    --rule: #b9bcc2;
    --white: #ffffff;
  }
  * { box-sizing: border-box; margin: 0; padding: 0; }
  html, body {
    width: 1200px; height: 1029px; overflow: hidden;
    background: var(--backdrop);
    font-family: "Quicksand", sans-serif;
  }
  .sheet {
    width: 1200px; height: 1029px;
    display: flex; flex-direction: column;
    align-items: center; justify-content: center; gap: 70px;
  }
  .card {
    position: relative;
    width: 700px; height: 400px;
    background: var(--card);
    box-shadow: 0 14px 30px rgba(0,0,0,0.12);
  }
  /* front */
  .card--front {
    display: flex; flex-direction: column;
    align-items: center; justify-content: center; gap: 22px;
  }
  .brand-mark {
    width: 150px; height: 150px; border-radius: 50%;
    background: var(--teal);
  }
  .brand-name {
    font-weight: 400; font-size: 34px; color: var(--teal);
    letter-spacing: 0.5px; white-space: nowrap;
  }
  /* back */
  .card--back { padding: 48px 0 0 56px; }
  .holder-name {
    font-weight: 700; font-size: 34px; line-height: 1.2; color: var(--ink);
    letter-spacing: 0.3px;
  }
  .holder-role {
    display: inline-block; margin-top: 4px;
    background: var(--teal); color: var(--white);
    font-weight: 400; font-size: 24px; line-height: 1.3;
    padding: 1px 90px 1px 14px;
  }
  .appointment {
    position: absolute; left: 56px; top: 158px; width: 350px;
    font-size: 14px; color: var(--ink);
  }
  .appointment-title {
    color: var(--teal); font-size: 14px; margin-bottom: 10px;
    letter-spacing: 0.5px;
  }
  .appointment-fields { display: flex; gap: 18px; }
  .appointment-field { display: flex; align-items: flex-end; gap: 8px; flex: 1; }
  .appointment-line { flex: 1; height: 16px; border-bottom: 1px solid var(--rule); }
  .contact {
    position: absolute; left: 56px; bottom: 36px;
    font-style: normal;
    font-size: 18px; line-height: 1.3; color: var(--ink-dark);
    white-space: nowrap;
  }
  .contact .accent, .contact .label { color: var(--teal); }
  .contact .label { display: inline-block; width: 56px; }
  .logo-lockup {
    position: absolute; right: 44px; top: 110px;
    display: flex; flex-direction: column; align-items: center; gap: 12px;
  }
  .logo-lockup .brand-mark { width: 110px; height: 110px; }
  .logo-lockup .brand-name { font-size: 21px; }
</style>
</head>
<body>
  <main class="sheet">
    <section class="card card--front">
      <div class="brand-mark"></div>
      <div class="brand-name">Marble Shore Dental</div>
    </section>

    <section class="card card--back">
      <h1 class="holder-name">Daniel R. Soto DDS</h1>
      <div class="holder-role">General Dentistry</div>

      <div class="appointment">
        <div class="appointment-title">Your next appointment</div>
        <div class="appointment-fields">
          <div class="appointment-field"><span>Date</span><span class="appointment-line"></span></div>
          <div class="appointment-field"><span>Time</span><span class="appointment-line"></span></div>
        </div>
      </div>

      <div class="logo-lockup">
        <div class="brand-mark"></div>
        <div class="brand-name">Marble Shore Dental</div>
      </div>

      <address class="contact">
        <div class="accent">1820 Harbor Crest Way</div>
        <div class="accent">Laguna Vista, CA 92700</div>
        <div>555-014-2828</div>
        <div><span class="label">email:</span>info@marbleshoredental.example</div>
        <div><span class="label">web:</span>www.marbleshoredental.example</div>
      </address>
    </section>
  </main>
</body>
</html>
```